Landing page graphical layout.

New landing page to capture leads from homeowners who are interested in learning the value of their home and/or selling their home.
The page should have a picture of a home in a residential area, possibly with a family standing outside.
This is the client's current site: http://homeworthpulse.com/
As you can see, it is very limited in terms of text and design, however once the user fills in the field it takes them to another page. The page's graphics should be enhanced with more calls to action as well as an additional field for the email address.
The client is a lead generator for real estate agents, so do not put the company name on the site as it will be used as a template for the client's various sites.
The forms need to be duplicated and inserted into the new design.
Some example sites:
http://www.brindlo.com/how-much-is-my-home-worth/
http://www.kptroost.com/home-valuation/?source=PROMO_SELLER&gclid=XQwerT_b-zzKLMnopqrS4B1
https://www.plovara.com/what-is-my-home-worth?estPropertyId=4190827&src=landing-page
Thanks!
Industry/Entity Type
Real Estate
Number of Pages Required
1 page
Look and feel

```html
<!DOCTYPE html>
<html lang="en">
<head>
<meta charset="utf-8">
<title>Home Value Estimate</title>
<link href="https://fonts.googleapis.com/css2?family=Open+Sans:wght@400;600;700;800&display=swap" rel="stylesheet">
<style>
  :root {
    --navy: #173a78;
    --navy-deep: #0f2c63;
    --sky: #3fb6e2;
    --sky-edge: #5cc6ec;
    --panel: #ebebeb;
    --ink: #2b2b2b;
    --muted: #6b6b6b;
    --field: #ffffff;
    --field-line: #d6d6d6;
    --alert: #ee1c25;
    --white: #ffffff;
  }
  * { box-sizing: border-box; margin: 0; padding: 0; }
  html, body { width: 882px; height: 1200px; overflow: hidden; }
  body { font-family: "Open Sans", Arial, sans-serif; background: var(--panel); position: relative; }

  .hero {
    position: absolute; left: 0; top: 0; width: 882px; height: 605px;
    background: linear-gradient(180deg, #8fb6d8 0%, #d9dde0 28%, #c9c2b4 55%, #7c9a5a 80%, #5f8a3c 100%);
  }
  .badge {
    position: absolute; left: 86px; top: 8px; width: 222px; height: 222px;
    border-radius: 50%; background: var(--navy-deep); border: 5px solid var(--white);
    color: var(--white); text-align: center; padding-top: 30px;
  }
  .badge svg { display: block; margin: 0 auto 6px; }
  .badge .line-small { font-size: 22px; font-weight: 600; line-height: 1.15; }
  .badge .line-big { font-size: 26px; font-weight: 800; line-height: 1.1; }

  .steps { position: absolute; top: 567px; left: 91px; display: flex; gap: 5px; }
  .step {
    width: 227px; height: 203px; background: var(--sky); color: var(--white);
    display: flex; flex-direction: column; align-items: center; justify-content: flex-end;
    padding-bottom: 38px;
  }
  .step.is-active { background: var(--navy); border: 4px solid var(--sky-edge); }
  .step svg { margin-bottom: 26px; }
  .step-label { font-size: 21px; font-weight: 600; letter-spacing: .3px; }

  .consult { position: absolute; top: 800px; left: 0; width: 882px; text-align: center; }
  .consult h1 { font-size: 34px; font-weight: 700; color: var(--ink); letter-spacing: .5px; }
  .consult p { font-size: 13px; color: var(--muted); width: 430px; margin: 8px auto 0; line-height: 1.5; }

  .lead-form { position: absolute; top: 895px; left: 197px; width: 488px; }
  .row { display: flex; gap: 15px; margin-bottom: 14px; }
  .field {
    flex: 1; height: 26px; background: var(--field); border: 1px solid var(--field-line);
    font-size: 10px; color: #999; padding: 6px 8px;
  }
  .field-label { font-size: 10.5px; color: var(--muted); margin: -4px 0 4px; }
  .field.area { height: 56px; }
  .submit {
    display: block; margin: 26px 0 0 171px; width: 147px; height: 30px;
    background: var(--alert); color: var(--white); font-family: inherit;
    font-size: 15px; font-weight: 700; border: none; letter-spacing: .4px;
  }

  .site-footer {
    position: absolute; bottom: 0; left: 0; width: 882px; height: 48px;
    background: var(--navy-deep); color: var(--white); font-size: 12px;
    display: flex; align-items: center; justify-content: center;
  }
</style>
</head>
<body>
  <div class="hero" role="img" aria-label="Photo of a smiling family of three sitting on the lawn in front of their suburban house"></div>

  <div class="badge">
    <svg width="48" height="42" viewBox="0 0 48 42"><path d="M24 2 L46 22 H40 V40 H8 V22 H2 Z" fill="#fff"/><rect x="18" y="24" width="12" height="16" fill="#0f2c63"/></svg>
    <div class="line-small">GET YOUR</div>
    <div class="line-big">HOME VALUE</div>
    <div class="line-small">ESTIMATE</div>
  </div>

  <div class="steps">
    <div class="step">
      <svg width="40" height="58" viewBox="0 0 40 58"><path d="M20 2 C9 2 2 10 2 20 C2 34 20 56 20 56 C20 56 38 34 38 20 C38 10 31 2 20 2 Z" fill="#fff"/><circle cx="20" cy="20" r="7" fill="#3fb6e2"/></svg>
      <span class="step-label">YOUR ADDRESS</span>
    </div>
    <div class="step is-active">
      <svg width="66" height="54" viewBox="0 0 66 54"><path d="M33 2 L64 28 H56 V52 H10 V28 H2 Z" fill="#3fb6e2"/><rect x="26" y="32" width="14" height="20" fill="#173a78"/><rect x="44" y="8" width="7" height="12" fill="#3fb6e2"/></svg>
      <span class="step-label">HOME INFORMATION</span>
    </div>
    <div class="step">
      <svg width="74" height="52" viewBox="0 0 74 52"><rect x="2" y="6" width="70" height="42" rx="3" fill="none" stroke="#fff" stroke-width="4"/><path d="M37 13 L54 28 H49 V40 H25 V28 H20 Z" fill="#fff"/></svg>
      <span class="step-label">HOME VALUE</span>
    </div>
  </div>

  <section class="consult">
    <h1>GET CONSULTATION</h1>
    <p>A local Agent can send you a professional comparative market analysis (CMA) for this home. It's free, with no obligation.</p>
  </section>

  <form class="lead-form">
    <div class="row"><div class="field">First Name</div><div class="field">Last Name</div></div>
    <div class="row"><div class="field">Email</div><div class="field">Phone</div></div>
    <div class="field-label">Prepare a Professional CMA for:</div>
    <div class="row"><div class="field"></div></div>
    <div class="row"><div class="field area">Comments/Notes</div></div>
    <button class="submit" type="button">SEND REQUEST</button>
  </form>

  <footer class="site-footer">© 2015, All rights reserved.</footer>
</body>
</html>
```